Brambleway Farming

We need a logo design for a new company based in Kelowna, BC. We grow market garden vegetables for sale at market and in a CSA program. We try to only use hand tools for all aspects of cultivating, seeding, weeding, harvesting and distributing. For this reason we consider ourselves very low impact on the environment.

We would like blues and green in the design with an earthy, natural feel

Target Market(s)

Environmentally aware, health conscience

Industry/Entity Type

Farming

Requirements
Must have
• Foot prints with section for contact details all on the one side
Should not have
• Dark, black colours or anything that looks unnatural

```html
<!DOCTYPE html>
<html lang="en">
<head>
<meta charset="utf-8">
<title>Brambleway Farming – Business Cards</title>
<link rel="stylesheet" href="https://fonts.googleapis.com/css2?family=Open+Sans:wght@400;600&display=swap">
<style>
  :root {
    --backdrop: #ecebe8;
    --card-white: #ffffff;
    --brand-blue: #0b76d3;
    --brand-green: #86bd0f;
    --text-white: #ffffff;
    --shadow: rgba(0, 0, 0, 0.18);
  }
  * { margin: 0; padding: 0; box-sizing: border-box; }
  html, body {
    width: 1200px; height: 900px; overflow: hidden;
    background: var(--backdrop);
    font-family: "Open Sans", sans-serif;
  }
  .canvas { position: relative; width: 1200px; height: 900px; }

  .card { position: absolute; box-shadow: 0 6px 18px var(--shadow); overflow: hidden; }

  /* Front card */
  .card-front { left: 77px; top: 34px; width: 588px; height: 364px; background: var(--card-white); }
  .front-bands { position: absolute; left: 0; top: 0; width: 588px; height: 364px; }
  .brand { position: absolute; display: flex; align-items: center; gap: 18px; }
  .brand-dot { width: 52px; height: 52px; border-radius: 50%; flex: none; }
  .brand-name { font-weight: 400; white-space: nowrap; letter-spacing: -0.3px; }
  .card-front .brand { left: 108px; top: 70px; }
  .card-front .brand-dot { background: var(--brand-blue); }
  .card-front .brand-name { font-size: 40px; color: var(--brand-green); }

  .person { position: absolute; right: 315px; top: 260px; text-align: right; color: var(--text-white); }
  .person-name { font-size: 19px; font-weight: 600; line-height: 26px; }
  .person-role { font-size: 15px; line-height: 22px; }

  .contact-list { position: absolute; left: 294px; top: 250px; list-style: none; color: var(--text-white); }
  .contact-item { display: flex; align-items: center; gap: 11px; font-size: 15px; height: 21px; }
  .contact-icon { width: 12px; height: 12px; fill: var(--text-white); flex: none; }
  .address { position: absolute; left: 105px; top: 322px; font-size: 15px; color: var(--text-white); }

  /* Back card */
  .card-back { left: 388px; top: 505px; width: 566px; height: 352px; background: var(--brand-blue); }
  .card-back .brand { left: 104px; top: 152px; }
  .card-back .brand-dot { background: var(--brand-green); }
  .card-back .brand-name { font-size: 34px; color: var(--text-white); }
  .tagline {
    position: absolute; left: 0; right: 0; top: 264px; text-align: center;
    color: var(--text-white); font-size: 16px; line-height: 22px; letter-spacing: 0.3px;
    text-transform: uppercase;
  }
</style>
</head>
<body>
<main class="canvas">

  <section class="card card-front" aria-label="Business card front">
    <svg class="front-bands" viewBox="0 0 588 364" aria-hidden="true">
      <polygon points="0,228 383,228 412,191 588,191 588,364 0,364" fill="var(--brand-blue)"/>
      <polygon points="0,199 402,199 380,226 0,226" fill="var(--brand-green)"/>
    </svg>
    <div class="brand">
      <span class="brand-dot"></span>
      <span class="brand-name">Brambleway Farming</span>
    </div>
    <div class="person">
      <p class="person-name">Daniel Harper</p>
      <p class="person-role">Managing Director</p>
    </div>
    <ul class="contact-list">
      <li class="contact-item">
        <svg class="contact-icon" viewBox="0 0 24 24"><path d="M6.6 10.8a15.1 15.1 0 0 0 6.6 6.6l2.2-2.2a1 1 0 0 1 1-.25 11.4 11.4 0 0 0 3.6.57 1 1 0 0 1 1 1V20a1 1 0 0 1-1 1A17 17 0 0 1 3 4a1 1 0 0 1 1-1h3.5a1 1 0 0 1 1 1c0 1.25.2 2.45.57 3.57a1 1 0 0 1-.25 1z"/></svg>
        044-555 010 246
      </li>
      <li class="contact-item">
        <svg class="contact-icon" viewBox="0 0 24 24"><path d="M2 5h20v14H2z" opacity="0"/><path d="M3 6h18v12H3zm2 2v.3l7 4.4 7-4.4V8l-7 4.3z"/></svg>
        hello@bramblewayfarm.ca
      </li>
      <li class="contact-item">
        <svg class="contact-icon" viewBox="0 0 24 24"><path d="M12 2a10 10 0 1 0 0 20 10 10 0 0 0 0-20zm6.9 6h-3a15.6 15.6 0 0 0-1.4-3.9A8 8 0 0 1 18.9 8zM12 4c.8 1.2 1.5 2.5 1.9 4h-3.8c.4-1.5 1.1-2.8 1.9-4zM4.3 14a8 8 0 0 1 0-4h3.4a16 16 0 0 0 0 4zm.8 2h3a15.6 15.6 0 0 0 1.4 3.9A8 8 0 0 1 5.1 16zm3-8h-3a8 8 0 0 1 4.4-3.9C8.9 5.3 8.4 6.6 8.1 8zM12 20c-.8-1.2-1.5-2.5-1.9-4h3.8c-.4 1.5-1.1 2.8-1.9 4zm2.3-6H9.7a14.7 14.7 0 0 1 0-4h4.6a14.7 14.7 0 0 1 0 4zm.2 5.9c.6-1.2 1.1-2.5 1.4-3.9h3a8 8 0 0 1-4.4 3.9zm1.8-5.9a16 16 0 0 0 0-4h3.4a8 8 0 0 1 0 4z"/></svg>
        www.bramblewayfarm.ca
      </li>
    </ul>
    <p class="address">4821 Orchard Lane, Kelowna BC, Canada, V1W 2K5.</p>
  </section>

  <section class="card card-back" aria-label="Business card back">
    <div class="brand">
      <span class="brand-dot"></span>
      <span class="brand-name">Brambleway Farming</span>
    </div>
    <p class="tagline">Cultivating, seeding, weeding<br>harvesting and distributing</p>
  </section>

</main>
</body>
</html>
```